IT Company requires new Business Card design.

Over the years we have had a few different business card designs. We are now due for new cards across the board for all staff. We felt this would be a good time to start fresh with a new design. Our traditional card simply had our details on the front, and a list of services on the back. We don't particularly need the list of services, we have had cards where the only thing on the rear of the card was our logo.
Feel free to be creative, we would like our tag line "Complete IT Management" to appear at some point, doesn't necessarily have to be with the logo.
I have attached samples and drafts of various previous cards we have used over the years.
Industry/Entity Type
Business
Look and feel
Each slider illustrates characteristics of the customer's brand and the style your logo design should communicate.

```html
<!DOCTYPE html>
<html lang="en">
<head>
<meta charset="utf-8">
<title>Harbour Systems — Business Card</title>
<link rel="stylesheet" href="https://fonts.googleapis.com/css2?family=Archivo+Black&family=Montserrat:wght@400;500&family=Roboto:wght@400;500&display=swap">
<style>
  :root {
    --page: #e4e4e4;
    --blue: #1b7cc6;
    --blue-deep: #0d62a8;
    --blue-bright: #3aa3e3;
    --ink: #1c1c1c;
    --ink-soft: #2a2a2a;
    --white: #f4f4f4;
    --muted: #cfcfcf;
  }
  * { box-sizing: border-box; margin: 0; padding: 0; }
  html, body { width: 1200px; height: 1200px; overflow: hidden; }
  body {
    background: var(--page);
    font-family: "Roboto", Arial, sans-serif;
    position: relative;
  }
  .card {
    position: absolute;
    top: 220px;
    width: 440px;
    height: 760px;
    overflow: hidden;
    box-shadow: 0 18px 40px rgba(0,0,0,0.18);
  }
  .card--front { left: 120px; background: var(--blue); }
  .card--back { left: 640px; background: var(--ink); }

  .card__texture {
    position: absolute; inset: 0;
  }
  .card--front .card__texture {
    background: linear-gradient(160deg, var(--blue-bright) 0%, var(--blue) 45%, var(--blue-deep) 100%);
  }
  .card--back .card__texture {
    background: linear-gradient(150deg, var(--ink-soft) 0%, var(--ink) 60%, #161616 100%);
  }

  /* Front */
  .front-mark {
    position: absolute;
    left: 110px; top: 120px;
    width: 220px; height: 220px;
    background: var(--white);
  }
  .front-wordmark {
    position: absolute;
    right: 30px; top: 430px;
    text-align: right;
    font-family: "Archivo Black", "Arial Black", sans-serif;
    color: var(--white);
    font-size: 60px;
    line-height: 0.95;
    letter-spacing: 0.5px;
  }
  .front-tagline {
    position: absolute;
    right: 30px; top: 560px;
    font-family: "Montserrat", Arial, sans-serif;
    font-weight: 400;
    color: var(--white);
    font-size: 15px;
    letter-spacing: 4.6px;
    text-transform: uppercase;
  }

  /* Back */
  .back-brand {
    position: absolute;
    right: 34px; top: 60px;
    display: flex; align-items: center; gap: 14px;
  }
  .back-brand__square {
    width: 70px; height: 70px; background: var(--blue-bright);
  }
  .back-brand__name {
    font-family: "Archivo Black", "Arial Black", sans-serif;
    color: var(--blue-bright);
    font-size: 32px;
    line-height: 0.95;
  }
  .back-tagline {
    position: absolute;
    right: 34px; top: 142px;
    font-family: "Montserrat", Arial, sans-serif;
    color: var(--blue-bright);
    font-size: 11px;
    letter-spacing: 2.6px;
    text-transform: uppercase;
  }
  .name-band {
    position: absolute;
    left: 0; top: 196px;
    width: 330px; height: 40px;
    background: var(--blue-bright);
    display: flex; align-items: center; justify-content: flex-end;
    padding-right: 18px;
  }
  .name-band__name {
    font-family: "Archivo Black", "Arial Black", sans-serif;
    color: var(--ink);
    font-size: 24px;
    letter-spacing: 0.5px;
  }
  .job-title {
    position: absolute;
    left: 0; top: 244px; width: 312px;
    text-align: right;
    color: var(--white);
    font-size: 17px;
  }
  .contact-list {
    position: absolute;
    left: 30px; top: 290px;
    list-style: none;
    color: var(--white);
    font-size: 17px;
    line-height: 24px;
  }
  .contact-list__item {
    display: flex; align-items: flex-start; gap: 12px;
  }
  .contact-list__item--gap { margin-bottom: 16px; }
  .contact-list__icon {
    flex: none; width: 18px; height: 18px; margin-top: 3px;
  }
  .contact-list__web-accent { color: var(--blue-bright); }
</style>
</head>
<body>

<section class="card card--front" aria-label="Card front">
  <div class="card__texture" role="img" aria-label="Blue gradient background with faint repeated company name pattern"></div>
  <div class="front-mark" aria-hidden="true"></div>
  <div class="front-wordmark">HARBOUR<br>SYSTEMS</div>
  <div class="front-tagline">Complete IT Management</div>
</section>

<section class="card card--back" aria-label="Card back">
  <div class="card__texture" role="img" aria-label="Dark charcoal background with faint large brand symbol and name pattern"></div>

  <div class="back-brand">
    <div class="back-brand__square" aria-hidden="true"></div>
    <div class="back-brand__name">HARBOUR<br>SYSTEMS</div>
  </div>
  <div class="back-tagline">Complete IT Management</div>

  <div class="name-band"><span class="name-band__name">DANIEL REYES</span></div>
  <div class="job-title">Web project Manager</div>

  <ul class="contact-list">
    <li class="contact-list__item contact-list__item--gap">
      <svg class="contact-list__icon" viewBox="0 0 18 18" aria-hidden="true">
        <circle cx="9" cy="9" r="9" fill="#5a5a5a"/>
        <path d="M9 4a3 3 0 0 0-3 3c0 2.3 3 6 3 6s3-3.7 3-6a3 3 0 0 0-3-3zm0 4.2a1.2 1.2 0 1 1 0-2.4 1.2 1.2 0 0 1 0 2.4z" fill="#f4f4f4"/>
      </svg>
      <span>Unit 4, 12 Corella Drive<br>Bibra Lake WA 6163</span>
    </li>
    <li class="contact-list__item">
      <svg class="contact-list__icon" viewBox="0 0 18 18" aria-hidden="true">
        <circle cx="9" cy="9" r="9" fill="#5a5a5a"/>
        <path d="M6 4.5l1.6 2.4-1 1a6 6 0 0 0 3.5 3.5l1-1 2.4 1.6-.8 1.5c-4 .2-7.9-3.7-7.7-7.7z" fill="#f4f4f4"/>
      </svg>
      <span>(08) 9300 1120</span>
    </li>
    <li class="contact-list__item">
      <svg class="contact-list__icon" viewBox="0 0 18 18" aria-hidden="true">
        <circle cx="9" cy="9" r="9" fill="#5a5a5a"/>
        <rect x="5" y="7" width="8" height="5" fill="#f4f4f4"/>
        <rect x="6.5" y="4.5" width="5" height="2" fill="#f4f4f4"/>
        <rect x="6.5" y="12.5" width="5" height="1.5" fill="#f4f4f4"/>
      </svg>
      <span>(08) 9300 1122</span>
    </li>
    <li class="contact-list__item">
      <svg class="contact-list__icon" viewBox="0 0 18 18" aria-hidden="true">
        <circle cx="9" cy="9" r="9" fill="#5a5a5a"/>
        <rect x="4.5" y="6" width="9" height="6.5" fill="#f4f4f4"/>
        <path d="M4.5 6l4.5 3.6L13.5 6" fill="none" stroke="#5a5a5a" stroke-width="1"/>
      </svg>
      <span>daniel@harboursystems.com.au</span>
    </li>
    <li class="contact-list__item">
      <svg class="contact-list__icon" viewBox="0 0 18 18" aria-hidden="true">
        <circle cx="9" cy="9" r="9" fill="#5a5a5a"/>
        <circle cx="9" cy="9" r="4.5" fill="none" stroke="#f4f4f4" stroke-width="1.2"/>
        <path d="M4.5 9h9M9 4.5c-2 2.5-2 6.5 0 9M9 4.5c2 2.5 2 6.5 0 9" fill="none" stroke="#f4f4f4" stroke-width="1"/>
      </svg>
      <span>www.<span class="contact-list__web-accent">harboursystems</span>.com.au</span>
    </li>
  </ul>
</section>

</body>
</html>
```